Opening new doors for every person - Solvane-Ridge

Please note that whoever will win this project , a 1on1 Powerpoint design project will separately be launched and will be offered to the winning designer.

---------
This letterhead is to provide proposals, as well as manuals for my clients.

I am looking for the letter, power point design and business card that inspires people when they see it, that they feel that design has been done with love and passion. Something that is professional, simple and yet creative, Business like, yet spiritual. That inspires growth!

This part of the branding for my company, therefore the business card as well as the power point design that will come after as 1on1 project should have the same team and feeling.

Solvane ridge, The company will be providing Coaching services (one-one or groups) to corporations, teams and individuals, partnering with them to achieve their goals/vision, by helping them to remove the self-imposed limiting beliefs, helping them to get them out of their own way, helping them to raise their level of consciousness and self-awareness.

The vision is: Bring conscious leadership to the workplace and to individuals for the wellbeing of humanity.

I know that somewhere out there will resonate with this, and will be inspired to provide the best design :) thank you very much!!!!!

MPORTANT:
- To use Free Fonts - let me know where I can download them
- Editable formats please for the double sized business card

LOGO is attached in pdf. If needed other file type please let me know

Thank you thank you in advance for your time and inspiration!! Sending good vibes for a great design out there

Must Have:
- Please keep on mind that the cards - power point will have the same feeling - Corporate branding
- that is not to heavy to look at it, that is simple and beautiful and inspiring
- Looking to have Calibri or Calibri light font

imple, yet inspirational - Professional, yet playful - business like, yet spiritual

I am looking for something different that the "standard" designs out there.

For example, the Logo of the company in the back side with a quote and the front side something simple, yet inspiring. that has the contact info as well as the social media details LinkedIn - Facebook - tweeter - website

Open for suggestions and inspiration :)

Thank you!

• - Please keep on mind that the cards - power point will have the same feeling
• - Corporate branding
• - that is not to heavy to look at it, that is simple and beautiful and inspiring
• - Looking to have Calibri or Calibri light font
• - Corporate colours as the logo

```html
<!DOCTYPE html>
<html lang="en">
<head>
<meta charset="utf-8">
<title>Solvane-Ridge Letterhead</title>
<link href="https://fonts.googleapis.com/css2?family=Lato:wght@400;700&display=swap" rel="stylesheet">
<style>
  :root {
    --navy: #2b4a8b;
    --gold: #fbbf0a;
    --paper: #ffffff;
    --backdrop: #d6d7d4;
    --ink: #4d5668;
  }
  * { margin: 0; padding: 0; box-sizing: border-box; }
  html, body { width: 1200px; height: 784px; overflow: hidden; }
  body {
    background: var(--backdrop);
    font-family: "Lato", Calibri, sans-serif;
    position: relative;
  }
  .letterhead {
    position: absolute;
    left: 320px; top: 30px;
    width: 560px; height: 724px;
    background: var(--paper);
    overflow: hidden;
  }
  .corner-art { position: absolute; left: 0; top: 0; }
  .accent-bar { position: absolute; height: 5px; }
  .accent-bar--navy { background: var(--navy); width: 28px; }
  .accent-bar--gold { background: var(--gold); width: 28px; }
  .brand {
    position: absolute; left: 34px; top: 30px;
    display: flex; align-items: center; gap: 10px;
  }
  .brand__dot {
    width: 30px; height: 30px; border-radius: 50%;
    background: var(--navy);
  }
  .brand__name {
    font-size: 15px; font-weight: 700; letter-spacing: 1px;
    color: var(--gold); text-transform: uppercase; line-height: 1;
  }
  .brand__tagline {
    font-size: 6.5px; font-weight: 700; letter-spacing: 0.8px;
    color: var(--navy); text-transform: uppercase; margin-top: 3px;
  }
  .contact {
    position: absolute; right: 28px; top: 30px;
    list-style: none; font-size: 7.5px; color: var(--ink); line-height: 1.45;
  }
  .contact li { display: flex; align-items: flex-start; gap: 5px; }
  .contact svg { width: 7px; height: 7px; margin-top: 2px; flex: none; }
</style>
</head>
<body>
  <main class="letterhead">
    <span class="accent-bar accent-bar--navy" style="left:34px; top:0;"></span>
    <span class="accent-bar accent-bar--gold" style="left:12px; top:10px;"></span>
    <span class="accent-bar accent-bar--navy" style="right:0; top:0; width:5px; height:22px;"></span>
    <span class="accent-bar accent-bar--gold" style="right:10px; top:0; width:5px; height:28px;"></span>

    <header class="brand">
      <span class="brand__dot"></span>
      <div>
        <div class="brand__name">Solvane-Ridge</div>
        <div class="brand__tagline">Clarity · Growth · Purpose</div>
      </div>
    </header>

    <ul class="contact">
      <li><svg viewBox="0 0 10 10"><path d="M5 0a3.5 3.5 0 0 0-3.5 3.5C1.5 6 5 10 5 10s3.5-4 3.5-6.5A3.5 3.5 0 0 0 5 0z" fill="var(--navy)"/></svg><span>24 Lantern Way, Suite 300<br>Brookfield, TX 77001</span></li>
      <li><svg viewBox="0 0 10 10"><path d="M2 0l2 2.5-1 1.5a6 6 0 0 0 3 3l1.5-1L10 8l-1.5 2C4 10 0 6 0 1.5z" fill="var(--navy)"/></svg><span>(000) 555-0142</span></li>
      <li><svg viewBox="0 0 10 10"><path d="M2 0l2 2.5-1 1.5a6 6 0 0 0 3 3l1.5-1L10 8l-1.5 2C4 10 0 6 0 1.5z" fill="var(--navy)"/></svg><span>(000) 555-0187</span></li>
      <li><svg viewBox="0 0 10 10"><rect x="0" y="2" width="10" height="6.5" fill="var(--navy)"/><path d="M0 2l5 3.5L10 2" stroke="#fff" fill="none"/></svg><span>hello@solvaneridge.com</span></li>
      <li><svg viewBox="0 0 10 10"><circle cx="5" cy="5" r="4.5" fill="var(--navy)"/></svg><span>www.solvaneridge.com</span></li>
    </ul>

    <svg class="corner-art" width="560" height="724" viewBox="0 0 560 724" aria-hidden="true">
      <polygon points="0,724 302,724 45,686 0,615" fill="var(--gold)"/>
      <polygon points="0,615 0,539 45,686" fill="var(--navy)"/>
      <rect x="0" y="717" width="560" height="7" fill="var(--navy)"/>
    </svg>
  </main>
</body>
</html>
```